Baufirma sucht Design für Schafkopfkarten
Zielgruppe
Wir sind eine Baufirma und suchen ein schlichtes Design für unsere Schafkopfkarten. Unsere Zielgruppe ist bunt gemischt
Aufgabenstellung
Wir suchen nach einem Design für Schafkopfkarten/Spielkarten.
- Kartenformat 56 x 100 mm
- weißer Rand
- Schlicht
- eventuell Retro Design
- Firmenlogo soll nicht verändert werden
- eventuell 'seit 1946' integrieren

```html
<!DOCTYPE html>
<html lang="de">
<head>
<meta charset="utf-8">
<title>Spielkarten – Varlheim</title>
<link rel="stylesheet" href="https://fonts.googleapis.com/css2?family=Lexend:wght@400;700&display=swap">
<style>
  :root {
    --stage: #dcdddc;
    --paper: #ffffff;
    --ink: #4f555b;
    --ink-soft: #6e7378;
    --accent: #fde02a;
    --accent-soft: #fdeb8a;
    --grid-minor: #efefef;
    --grid-major: #e3e3e3;
    --label: #2b2b2b;
  }
  * { box-sizing: border-box; margin: 0; padding: 0; }
  html, body { width: 1200px; height: 947px; overflow: hidden; }
  body {
    background: var(--stage);
    font-family: "Lexend", Arial, sans-serif;
    position: relative;
  }
  .variant-label {
    position: absolute;
    top: 22px;
    font-size: 46px;
    font-weight: 400;
    color: var(--label);
    font-family: Arial, Helvetica, sans-serif;
  }
  .variant-label--one { left: 34px; }
  .variant-label--two { left: 635px; }

  .card {
    position: absolute;
    top: 65px;
    width: 470px;
    height: 816px;
    background: var(--paper);
    border-radius: 39px;
  }
  .card--back { left: 78px; }
  .card--face { left: 682px; }

  .card-field {
    position: absolute;
    left: 31px;
    top: 32px;
    width: 408px;
    height: 753px;
    border: 1px solid var(--ink);
    border-radius: 22px;
    overflow: hidden;
  }

  .pattern-fill {
    width: 100%;
    height: 100%;
    background:
      linear-gradient(135deg, rgba(253,224,42,0.35), rgba(79,85,91,0.35) 50%, rgba(253,224,42,0.35)),
      #f1f1ee;
  }

  .card-field--grid {
    background-color: var(--paper);
    background-image:
      repeating-linear-gradient(90deg, var(--grid-major) 0 3px, transparent 3px 78px),
      repeating-linear-gradient(0deg, var(--grid-major) 0 3px, transparent 3px 78px),
      repeating-linear-gradient(90deg, var(--grid-minor) 0 1px, transparent 1px 15.6px),
      repeating-linear-gradient(0deg, var(--grid-minor) 0 1px, transparent 1px 15.6px);
    background-position: 47px 0, 0 62px, 0 0, 0 0;
  }

  .brand-half {
    position: absolute;
    left: 0;
    width: 100%;
    height: 376px;
  }
  .brand-half--top { top: 0; }
  .brand-half--bottom { bottom: 0; transform: rotate(180deg); }

  .since {
    position: absolute;
    left: 12px;
    top: 12px;
    padding: 2px 6px;
    background: var(--paper);
    border-radius: 6px;
    font-size: 14px;
    color: var(--ink);
  }

  .mark-pad {
    position: absolute;
    left: 154px;
    top: 60px;
    width: 100px;
    height: 100px;
    background: var(--paper);
    border-radius: 14px;
    display: flex;
    align-items: center;
    justify-content: center;
  }
  .mark-square {
    width: 56px;
    height: 56px;
    background: var(--accent);
  }

  .name-pad {
    position: absolute;
    left: 38px;
    top: 153px;
    width: 332px;
    height: 86px;
    background: var(--paper);
    border-radius: 10px;
    text-align: center;
  }
  .company-name {
    display: block;
    margin-top: 8px;
    font-size: 38px;
    font-weight: 700;
    letter-spacing: 3px;
    line-height: 44px;
    color: var(--ink);
  }
  .services {
    display: block;
    margin-top: 6px;
    font-size: 15px;
    font-weight: 400;
    letter-spacing: 1px;
    color: var(--ink-soft);
  }
  .services .divider { color: var(--accent); margin: 0 6px; }

  .split-line {
    position: absolute;
    left: 0;
    top: 0;
  }
</style>
</head>
<body>
  <div class="variant-label variant-label--one">1.</div>
  <div class="variant-label variant-label--two">2.</div>

  <section class="card card--back">
    <div class="card-field">
      <div class="pattern-fill" role="img" aria-label="Kartenrückseite mit wiederholtem Sechseck-Muster in Grau und Gelb auf Rasterpapier"></div>
    </div>
  </section>

  <section class="card card--face">
    <div class="card-field card-field--grid">
      <svg class="split-line" width="408" height="753" viewBox="0 0 408 753" aria-hidden="true">
        <line x1="0" y1="456" x2="408" y2="298" stroke="#2f3336" stroke-width="1.3"/>
        <line x1="0" y1="461" x2="408" y2="303" stroke="#2f3336" stroke-width="1.3"/>
      </svg>

      <div class="brand-half brand-half--top">
        <span class="since">seit 1946</span>
        <div class="mark-pad"><span class="mark-square"></span></div>
        <div class="name-pad">
          <span class="company-name">VARLHEIM</span>
          <span class="services">TIEFBAU<span class="divider">//</span>ABBRUCH<span class="divider">//</span>RECYCLING</span>
        </div>
      </div>

      <div class="brand-half brand-half--bottom">
        <span class="since">seit 1946</span>
        <div class="mark-pad"><span class="mark-square"></span></div>
        <div class="name-pad">
          <span class="company-name">VARLHEIM</span>
          <span class="services">TIEFBAU<span class="divider">//</span>ABBRUCH<span class="divider">//</span>RECYCLING</span>
        </div>
      </div>
    </div>
  </section>
</body>
</html>
```